Esoteric, wellness company labels

Verdant Lumen is a lifestyle brand with multiple products. We have an offshoot as well called Lumen Coffee. I need multiple labels or packaging designs that all match so I can start wholesaling.

I want something fun and very eye catching. I have two different logos for Verdant Lumen but just one for the coffee. I’m
Undecided which one I want on the labels because I like both. So either would work. Any coffee products go under lumen coffee and any other products go under Verdant Lumen.

We sell items such as crystals, tarot and oracle decks, candles, organic coffee, superfood powders and herbs and more.

The items I need labels for should have a streamline look so that all are recognizable as the Verdant Lumen brand. The products that are a priority are:
Organic coffee
Reishi infused coffee
Lion’s Mane infused coffee
Those go under Lumen Coffee.

Soon I’ll do more items;
Sacred smudging spray
Sacred smudging cleaner
Multiple superfoods
Etc
Updates

We have decided to use compostable coffee bags that are approximately 9x6x33cm so your standard 1lb bag you would see in a store. We still want colorful and eye catching but at the same time being eco friendly. The coffee is 100% organic, free trade, low acid.

We are looking for labels for the coffee but also want to be able to use the same kind of design or similar down the road for our other products. We carry superfood powders (lion’s mane, blue Spirulina, reishi, pearl powder, sea moss etc) but also things like smudging spray, rose water, neroli water, essential oils etc. we are a lifestyle company so we are looking for labels across our store brand items.

Target Market(s)

Esoteric, health and wellness, “new age”

Industry/Entity Type

Retail, wellness,

Colors

Designer to choose colors to be used in the design.

Requirements
Must have
• Beauty, attraction
Should not have
• Anything to do with religion, no dark witchy themes

```html
<!DOCTYPE html>
<html lang="en">
<head>
<meta charset="utf-8">
<title>Lumen Coffee Labels</title>
<link rel="stylesheet" href="https://fonts.googleapis.com/css2?family=Abril+Fatface&family=Cormorant+Garamond:wght@500;700&family=Lato:wght@700&display=swap">
<style>
  :root {
    --navy: #1b2842;
    --cream: #f4e4d0;
    --title-shadow: #b79f86;
    --ink: #2a2a2a;
    --rust: #b8593a;
    --rust-glow: #d89576;
    --sage: #5c7639;
    --sage-glow: #93a96c;
    --sand: #b9a66a;
    --sand-glow: #dcc995;
    --arch-sky: #1c2844;
    --arch-edge: #8a93a8;
  }
  * { margin: 0; padding: 0; box-sizing: border-box; }
  html, body { width: 906px; height: 1200px; overflow: hidden; background: #ffffff; }
  .sheet { position: relative; width: 906px; height: 1200px; }

  .dimension { position: absolute; font-family: "Lato", sans-serif; font-weight: 700; color: var(--ink); font-size: 11px; }
  .dimension-width { left: 329px; top: 382px; width: 248px; text-align: center; }
  .dimension-width-line { position: absolute; left: 329px; top: 407px; width: 248px; height: 1px; background: #3b4656; }
  .dimension-height-line { position: absolute; left: 593px; top: 440px; width: 1px; height: 361px; background: #3b4656; }
  .dimension-height { left: 602px; top: 620px; transform: rotate(90deg); transform-origin: left top; white-space: nowrap; }

  .label { position: absolute; top: 440px; width: 248px; height: 361px; overflow: hidden; }
  .label-organic { left: 25px; background: radial-gradient(ellipse at 50% 55%, var(--rust-glow) 0%, var(--rust) 65%); }
  .label-reishi { left: 329px; background: radial-gradient(ellipse at 50% 50%, var(--sage-glow) 0%, var(--sage) 65%); }
  .label-lions-mane { left: 633px; background: radial-gradient(ellipse at 50% 55%, var(--sand-glow) 0%, var(--sand) 70%); }

  .label-frame { position: absolute; left: 12px; top: 12px; right: 12px; bottom: 12px; border: 1px solid var(--navy); border-radius: 10px; }
  .label-frame::after { content: ""; position: absolute; inset: 3px; border: 1.5px dotted rgba(244,228,208,0.8); border-radius: 8px; }

  .brand-tab { position: absolute; left: 94px; top: 0; width: 60px; height: 55px; background: var(--navy); display: flex; flex-direction: column; align-items: center; justify-content: center; gap: 5px; z-index: 2; }
  .brand-dot { width: 12px; height: 12px; border: 1px solid var(--cream); border-radius: 50%; }
  .brand-name { font-family: "Cormorant Garamond", serif; font-weight: 500; font-size: 7px; letter-spacing: 1px; color: var(--cream); text-align: center; line-height: 1.1; }

  .arch-scene { position: absolute; left: 79px; top: 75px; width: 91px; height: 125px; border-radius: 46px 46px 0 0; background: linear-gradient(100deg, var(--arch-edge) 0%, var(--arch-sky) 35%, var(--arch-sky) 100%); box-shadow: -3px -2px 0 #8c8079; }

  .product-title { position: absolute; left: 0; right: 0; top: 160px; text-align: center; font-family: "Abril Fatface", serif; font-size: 34px; line-height: 29px; color: var(--cream); text-shadow: 2px 2px 0 var(--title-shadow); letter-spacing: -0.5px; z-index: 1; }

  .product-variant { position: absolute; left: 0; right: 0; top: 250px; text-align: center; font-family: "Cormorant Garamond", serif; font-weight: 500; font-size: 13px; color: var(--cream); text-transform: uppercase; }
  .label-lions-mane .product-variant { font-size: 9.5px; top: 253px; }
  .product-form { position: absolute; left: 0; right: 0; top: 268px; display: flex; align-items: center; justify-content: center; gap: 4px; font-family: "Cormorant Garamond", serif; font-weight: 700; font-size: 7px; color: var(--cream); letter-spacing: 0.3px; }
  .product-form::before, .product-form::after { content: ""; width: 18px; height: 1px; background: var(--cream); }

  .net-weight { position: absolute; left: 0; right: 0; top: 314px; text-align: center; font-family: "Cormorant Garamond", serif; font-weight: 500; font-size: 9.5px; color: rgba(244,228,208,0.75); }

  .web-tab { position: absolute; left: 64px; bottom: 0; width: 121px; height: 25px; background: var(--navy); display: flex; align-items: center; justify-content: center; font-family: "Cormorant Garamond", serif; font-weight: 700; font-size: 8px; letter-spacing: 1px; color: var(--cream); z-index: 2; }
</style>
</head>
<body>
<main class="sheet">
  <div class="dimension dimension-width">2.75 INCH</div>
  <div class="dimension-width-line"></div>
  <div class="dimension-height-line"></div>
  <div class="dimension dimension-height">4 INCH</div>

  <section class="label label-organic">
    <div class="label-frame"></div>
    <div class="brand-tab"><span class="brand-dot"></span><span class="brand-name">VERDANT<br>LUMEN</span></div>
    <div class="arch-scene" role="img" aria-label="Arched night window with crescent moon, star, blue leaves and stairs"></div>
    <h2 class="product-title">LUMEN<br>COFFEE</h2>
    <p class="product-variant">Organic Coffee</p>
    <p class="product-form">WHOLE BEANS</p>
    <p class="net-weight">250 G / 8.8 OZ</p>
    <div class="web-tab">VERDANTLUMEN.COM</div>
  </section>

  <section class="label label-reishi">
    <div class="label-frame"></div>
    <div class="brand-tab"><span class="brand-dot"></span><span class="brand-name">VERDANT<br>LUMEN</span></div>
    <div class="arch-scene" role="img" aria-label="Arched night window with crescent moon, star, blue leaves and stairs"></div>
    <h2 class="product-title">LUMEN<br>COFFEE</h2>
    <p class="product-variant">Reishi Infused Coffee</p>
    <p class="product-form">WHOLE BEANS</p>
    <p class="net-weight">250 G / 8.8 OZ</p>
    <div class="web-tab">VERDANTLUMEN.COM</div>
  </section>

  <section class="label label-lions-mane">
    <div class="label-frame"></div>
    <div class="brand-tab"><span class="brand-dot"></span><span class="brand-name">VERDANT<br>LUMEN</span></div>
    <div class="arch-scene" role="img" aria-label="Arched night window with crescent moon, star, blue leaves and stairs"></div>
    <h2 class="product-title">LUMEN<br>COFFEE</h2>
    <p class="product-variant">Lion’s Mane Infused Coffee</p>
    <p class="product-form">WHOLE BEANS</p>
    <p class="net-weight">250 G / 8.8 OZ</p>
    <div class="web-tab">VERDANTLUMEN.COM</div>
  </section>
</main>
</body>
</html>
```